Corporate Business Card

Very professional, Modern, Not to busy, include phone address email, website
(253) 555-0174, 61807 19th Street N, Kent, WA 98517, marcus@kestrelbayholding.com, brelvanindustries.com

Target Market(s)

Manufacturing

Industry/Entity Type

Aero, machining, manufacturing, Off road racing

Contact Information for Business Card

Phone, address email, website

```html
<!DOCTYPE html>
<html lang="en">
<head>
<meta charset="utf-8">
<title>Brelvan Industries – Business Card</title>
<link rel="stylesheet" href="https://fonts.googleapis.com/css2?family=Open+Sans:wght@400;700&family=Ubuntu:wght@500;700&display=swap">
<style>
  :root {
    --brand-red: #d1232a;
    --brand-navy: #18356b;
    --paper: #ffffff;
    --ink-dark: #231f20;
  }
  * { margin: 0; padding: 0; box-sizing: border-box; }
  html, body { width: 1200px; height: 1200px; overflow: hidden; }
  body { position: relative; background: var(--brand-red); font-family: "Ubuntu", sans-serif; }

  .backdrop { position: absolute; inset: 0; width: 1200px; height: 1200px; }

  .card {
    position: absolute;
    left: 209px;
    width: 783px;
    height: 447px;
    border-radius: 47px;
    overflow: hidden;
    background: var(--paper);
  }
  .card--front { top: 101px; box-shadow: 0 6px 14px rgba(0,0,0,0.28); }
  .card--back { top: 651px; }
  .card__shapes { position: absolute; inset: 0; width: 100%; height: 100%; }

  .holder { position: absolute; left: 100px; top: 88px; }
  .holder__name {
    font-family: "Open Sans", sans-serif;
    font-weight: 700;
    font-size: 40px;
    line-height: 1;
    color: var(--ink-dark);
    letter-spacing: 0.2px;
  }
  .holder__role {
    font-family: "Open Sans", sans-serif;
    font-weight: 400;
    font-size: 15px;
    line-height: 1;
    color: var(--paper);
    margin-top: 2px;
  }

  .contact-list { position: absolute; left: 72px; top: 252px; list-style: none; }
  .contact-list__item {
    display: flex;
    align-items: center;
    height: 25px;
    margin-bottom: 11px;
    color: var(--paper);
    font-weight: 500;
    font-size: 21.5px;
    white-space: nowrap;
  }
  .contact-list__icon {
    width: 25px; height: 25px;
    background: var(--brand-red);
    margin-right: 13px;
    flex: none;
  }
  .contact-list__icon svg { display: block; width: 25px; height: 25px; }

  .wordmark { position: absolute; color: var(--brand-navy); font-weight: 700; text-align: right; line-height: 1; }
  .wordmark__name { display: block; }
  .wordmark__sub { display: block; }
  .wordmark--front { right: 48px; top: 56px; }
  .wordmark--front .wordmark__name { font-size: 48px; letter-spacing: 1px; }
  .wordmark--front .wordmark__sub { font-size: 18px; letter-spacing: 4px; margin-top: 6px; }

  .wordmark--back { left: 0; right: 0; top: 130px; text-align: center; }
  .wordmark--back .wordmark__name { font-size: 92px; letter-spacing: 3px; }
  .wordmark--back .wordmark__sub { font-size: 30px; letter-spacing: 9px; margin-top: 14px; }

  .card__url {
    position: absolute;
    left: 97px;
    top: 412px;
    color: var(--paper);
    font-weight: 500;
    font-size: 22px;
    line-height: 1;
  }
</style>
</head>
<body>
  <svg class="backdrop" viewBox="0 0 1200 1200" aria-hidden="true">
    <rect width="1200" height="1200" fill="var(--brand-red)"/>
    <polygon points="1200,0 1200,1200 0,1200" fill="var(--brand-navy)"/>
  </svg>

  <section class="card card--front" aria-label="Business card front">
    <svg class="card__shapes" viewBox="0 0 1260 720" preserveAspectRatio="none" aria-hidden="true">
      <path d="M0,0 L432,0 L830,400 L830,555 L608,720 L0,720 Z" fill="var(--brand-navy)"/>
      <path d="M119,88 L470,88 C540,88 575,100 608,133 L830,350 C865,385 877,420 877,455 C877,495 860,525 830,555 L655,720 L0,720 L0,280 L119,280 Z" fill="var(--brand-red)"/>
      <path d="M0,280 L665,280 C700,280 725,290 745,310 L800,365 C830,395 845,425 845,455 C845,485 830,510 800,540 L608,720 L0,720 Z" fill="var(--brand-navy)"/>
    </svg>

    <div class="holder">
      <div class="holder__name">YOUR NAME</div>
      <div class="holder__role">Designation</div>
    </div>

    <ul class="contact-list">
      <li class="contact-list__item">
        <span class="contact-list__icon"><svg viewBox="0 0 25 25" aria-hidden="true"><path d="M12.5 4a5 5 0 0 1 5 5c0 3.6-5 9-5 9s-5-5.4-5-9a5 5 0 0 1 5-5z" fill="#fff"/><circle cx="12.5" cy="9" r="1.9" fill="var(--brand-red)"/><ellipse cx="12.5" cy="20" rx="4" ry="1.2" fill="none" stroke="#fff" stroke-width="1"/></svg></span>
        61807 19th Street N, Kent, WA 98517
      </li>
      <li class="contact-list__item">
        <span class="contact-list__icon"><svg viewBox="0 0 25 25" aria-hidden="true"><path d="M7 5.5l2.6-.5 1.6 3.6-1.8 1.3c.9 2 2.4 3.5 4.3 4.4l1.3-1.8 3.6 1.6-.5 2.6c-.3 1-1.3 1.6-2.3 1.4C10.4 17.1 7 13.7 6 8.3c-.2-1.1.3-2.3 1-2.8z" fill="#fff"/><path d="M14 6.5a4.5 4.5 0 0 1 4.5 4.5M14 4a7 7 0 0 1 7 7" fill="none" stroke="#fff" stroke-width="1.1"/></svg></span>
        (253) 555-0174
      </li>
      <li class="contact-list__item">
        <span class="contact-list__icon"><svg viewBox="0 0 25 25" aria-hidden="true"><rect x="4.5" y="7.5" width="16" height="10" fill="#fff"/><path d="M4.5 7.5l8 6 8-6M4.5 17.5l6-5M20.5 17.5l-6-5" fill="none" stroke="var(--brand-red)" stroke-width="1.1"/></svg></span>
        marcus@kestrelbayholding.com
      </li>
      <li class="contact-list__item">
        <span class="contact-list__icon"><svg viewBox="0 0 25 25" aria-hidden="true"><g fill="none" stroke="#fff" stroke-width="1.1"><circle cx="12.5" cy="12.5" r="8"/><ellipse cx="12.5" cy="12.5" rx="3.5" ry="8"/><path d="M4.5 12.5h16M5.8 8.5h13.4M5.8 16.5h13.4"/></g></svg></span>
        www.brelvanindustries.com
      </li>
    </ul>

    <div class="wordmark wordmark--front">
      <span class="wordmark__name">BRELVAN</span>
      <span class="wordmark__sub">INDUSTRIES</span>
    </div>
  </section>

  <section class="card card--back" aria-label="Business card back">
    <svg class="card__shapes" viewBox="0 0 1260 720" preserveAspectRatio="none" aria-hidden="true">
      <path d="M0,647 L665,647 C700,647 725,657 745,677 L788,720 L0,720 Z" fill="var(--brand-navy)"/>
      <path d="M762,685 L1260,685 L1260,720 L797,720 Z" fill="var(--brand-red)"/>
    </svg>

    <div class="wordmark wordmark--back">
      <span class="wordmark__name">BRELVAN</span>
      <span class="wordmark__sub">INDUSTRIES</span>
    </div>

    <div class="card__url">www.brelvanindustries.com</div>
  </section>
</body>
</html>
```